Lumora Business Card Design

hello,
we are looking for a business card design for our Fintech Company. We are credit card processing company that is also expanding in to the crypto market. We will be focusing on crypto processing, with a crypto wallet and crypto exchange. We like the purple in the logo. We want something modern and sophisticated but at the same time simple and trust worthy to work with banks.

Industry/Entity Type

Fintech

Logo Text

Lumora

```html
<!DOCTYPE html>
<html lang="en">
<head>
<meta charset="utf-8">
<title>Lumora Business Card</title>
<link href="https://fonts.googleapis.com/css2?family=Inter:wght@600&display=swap" rel="stylesheet">
<style>
  :root {
    --purple: #6a3dff;
    --blue: #2a9bf2;
    --paper: #ffffff;
    --canvas: #fdfdfd;
  }
  html, body {
    margin: 0;
    width: 1200px;
    height: 1200px;
    overflow: hidden;
    background: var(--canvas);
  }
  .card {
    position: absolute;
    top: 489px;
    width: 386px;
    height: 222px;
    background: var(--paper);
    box-sizing: border-box;
    border: 2px solid var(--purple);
    overflow: hidden;
  }
  .card--back { left: 199px; }
  .card--front { left: 614px; }
  .card-art {
    position: absolute;
    inset: 0;
    width: 100%;
    height: 100%;
  }
  .wordmark {
    position: absolute;
    left: 0;
    right: 0;
    margin: 0;
    text-align: center;
    font-family: "Inter", sans-serif;
    font-weight: 600;
    color: var(--purple);
    letter-spacing: -0.5px;
    line-height: 1;
  }
  .card--back .wordmark { top: 42px; font-size: 38px; left: -4px; }
  .card--front .wordmark { top: 83px; font-size: 60px; }
</style>
</head>
<body>

<section class="card card--back">
  <svg class="card-art" viewBox="0 0 483 277" aria-hidden="true">
    <g class="contact-icons" fill="none" stroke="var(--purple)" stroke-width="2" stroke-linecap="round" stroke-linejoin="round">
      <path d="M44 128 C37 120 37 113 44 111 C51 113 51 120 44 128Z"/>
      <circle cx="44" cy="117" r="2.2"/>
      <path d="M42 148 C39 151 41 158 47 161 L49 159 L46 156 L44 157 C43 155 42 153 43 151 L44 150 Z" fill="var(--purple)" stroke-width="1"/>
      <rect x="35" y="177" width="19" height="13" rx="1"/>
      <path d="M35 178 L44.5 185 L54 178"/>
      <circle cx="44" cy="217" r="7.5"/>
      <path d="M36.5 217 H51.5 M44 209.5 C40 213 40 221 44 224.5 C48 221 48 213 44 209.5 M38 213 H50 M38 221 H50" stroke-width="1.4"/>
    </g>
    <path d="M0 240 H220 C232 240 236 262 255 263 H483 V277 H0Z" fill="var(--purple)"/>
    <path d="M243 249 H483 V257 H258 C250 257 247 253 243 249Z" fill="var(--blue)"/>
  </svg>
  <p class="wordmark">Lumora</p>
</section>

<section class="card card--front">
  <svg class="card-art" viewBox="0 0 483 277" aria-hidden="true">
    <path d="M0 240 H220 C232 240 236 262 255 263 H483 V277 H0Z" fill="var(--purple)"/>
    <path d="M243 249 H483 V257 H258 C250 257 247 253 243 249Z" fill="var(--blue)"/>
  </svg>
  <p class="wordmark">Lumora</p>
</section>

</body>
</html>
```